Tax Preparation flyer for LedgerMint Corp.

My Client would like a one page PDF flyer to promote upcoming tax season in Canada. This firm is affordable and all virtual. I have attached a copy of their logo and a word document with the proposed wording for the flyer. Please feel free to change if you have better suggestions.

Target Market(s)

individuals in canada

Colors
0054AA
0677BA
7BADD7
CADEEF
E8F1F8

```html
<!DOCTYPE html>
<html lang="en">
<head>
<meta charset="utf-8">
<title>LedgerMint Corp. – Tax Season Flyer</title>
<link href="https://fonts.googleapis.com/css2?family=Poppins:wght@400;500;600;700;800&display=swap" rel="stylesheet">
<style>
  :root{
    --navy:#0b2c45;
    --deep:#0b4a74;
    --blue:#0b93d6;
    --band:#0a7bbd;
    --sky:#e3f2fb;
    --ink:#111111;
    --white:#ffffff;
    --stage:#ecebe8;
  }
  *{margin:0;padding:0;box-sizing:border-box}
  html,body{width:1200px;height:1117px;overflow:hidden;background:var(--stage);font-family:"Poppins",sans-serif}
  .flyer{position:absolute;left:219px;top:20px;width:761px;height:1077px;background:var(--white);overflow:hidden}
  .flyer > *{position:absolute}
  .shapes{left:0;top:0;width:761px;height:1077px}
  .photo{left:0;top:0;width:761px;height:270px}
  .headline{left:20px;top:38px;width:390px;text-align:center;color:var(--navy);font-weight:800;line-height:1}
  .headline .line{display:block;font-size:39px;letter-spacing:.5px}
  .headline .big{display:block;font-size:94px;color:var(--blue);letter-spacing:-1px;margin:-2px 0 -4px}
  .brand{left:530px;top:22px;width:200px;text-align:right;color:var(--navy);font-weight:700;font-size:32px;line-height:1.05}
  .intro{left:34px;top:266px;width:696px;height:181px;background:var(--deep);border-radius:14px;padding:20px 24px;color:var(--white);font-size:12.2px;line-height:1.12}
  .intro p{margin-bottom:13px}
  .intro .p-lead{max-width:648px}
  .intro .p-portal{max-width:595px}
  .intro .p-meet{max-width:560px}
  .money{left:672px;top:376px;width:89px;height:110px}
  .pricing{left:75px;top:474px;color:var(--white);font-weight:700;font-size:48px;line-height:1}
  .pricing small{display:block;font-weight:400;font-size:13px;margin:-2px 0 0 22px}
  .price{left:296px;top:448px;font-weight:800;font-size:104px;letter-spacing:-4px;color:var(--deep);-webkit-text-stroke:10px var(--white);paint-order:stroke fill;line-height:1.1}
  .addon{left:0;top:569px;width:761px;padding-left:30px;text-align:center;color:var(--blue);font-weight:700;font-size:15.8px}
  .details{left:59px;top:614px;width:630px;color:var(--ink);font-size:12.3px;line-height:1.2}
  .details p{margin-bottom:14px}
  .cta{left:59px;top:746px;width:630px;display:flex;align-items:center;font-size:12.3px;color:var(--ink)}
  .cta strong{color:var(--blue);font-size:19px;font-weight:700;margin-left:5px}
  .cta .rule{flex:1;height:2px;background:var(--blue);margin-left:16px}
  .bookkeeping{left:60px;top:800px;width:641px;text-align:center;color:var(--deep)}
  .bookkeeping h2{font-size:16px;font-weight:700;line-height:1.2}
  .bookkeeping .feel{margin-top:16px;font-size:13.4px;line-height:1.45;color:var(--deep)}
  .bookkeeping .feel strong{font-size:18.5px;font-weight:700}
  .bookkeeping .note{margin:12px auto 0;width:570px;font-size:11.6px;line-height:1.25}
  .contact-label{left:58px;top:1024px;color:var(--white);font-weight:700;font-size:25px}
  .contact{left:272px;top:1025px;display:flex;align-items:center;color:var(--white);font-weight:700;font-size:19.5px}
  .contact .item{display:flex;align-items:center;gap:8px}
  .contact .divider{width:2px;height:36px;background:var(--white);margin:0 18px}
  .contact svg{width:24px;height:24px}
</style>
</head>
<body>
<main class="flyer">
  <svg class="shapes" viewBox="0 0 761 1077" aria-hidden="true">
    <polygon points="0,229 424,262 761,262 761,513 0,513" fill="#0b93d6"/>
    <rect x="0" y="470" width="310" height="87" fill="#0a7bbd"/>
    <rect x="0" y="789" width="761" height="288" fill="#e3f2fb"/>
    <polygon points="0,1017 761,990 761,1077 0,1077" fill="#0b93d6"/>
    <polygon points="0,1004 230,1004 250,1077 0,1077" fill="#0b4a74"/>
  </svg>

  <svg class="photo" viewBox="0 0 761 270" role="img" aria-label="Photo of an advisor cupping hands over a small model house on a desk with books">
    <defs>
      <linearGradient id="photoTone" x1="0" y1="0" x2="1" y2="1">
        <stop offset="0" stop-color="#c9d2d9"/>
        <stop offset=".55" stop-color="#eef1f3"/>
        <stop offset="1" stop-color="#5b636b"/>
      </linearGradient>
    </defs>
    <polygon points="390,0 761,0 761,270 424,262" fill="url(#photoTone)"/>
  </svg>

  <h1 class="headline">
    <span class="line">RELAX, WE’VE</span>
    <span class="line">GOT YOUR</span>
    <span class="big">TAXES</span>
    <span class="line">COVERED!</span>
  </h1>

  <div class="brand">LedgerMint<br>Corp.</div>

  <section class="intro">
    <p class="p-lead">Our tax preparers have over 20 years experience and worked both in public accounting firms as well as specialized tax. Our tax services are virtual, so you don’t have to take the time for a personal visit. We take care of everything and can access all your tax slips from TaxGate website directly into our tax software. All signing is done via SignVault.</p>
    <p class="p-portal">You can fill and submit the appropriate forms, along with all your other documents, in our secure client portal. It’s important that we understand your situation and any changes in your situation from the past year.</p>
    <p class="p-meet">If you have a complex tax situation and would like to discuss it, we can meet in virtually over MeetWave or LinkRoom</p>
  </section>

  <svg class="money" viewBox="0 0 89 110" role="img" aria-label="Illustration of green banknotes">
    <defs>
      <linearGradient id="cash" x1="0" y1="0" x2="1" y2="1">
        <stop offset="0" stop-color="#b9c98a"/>
        <stop offset="1" stop-color="#5f8a4a"/>
      </linearGradient>
    </defs>
    <polygon points="40,6 78,0 89,28 89,110 24,110 0,78" fill="url(#cash)"/>
  </svg>

  <div class="pricing">Pricing<small>Personal Tax Return</small></div>
  <div class="price">$100.00</div>

  <p class="addon">Add a business or rental schedule $125 per business or rental property.</p>

  <section class="details">
    <p>More complex tax returns will be assessed based on the complexity of the return and you will be advised before we start.</p>
    <p>Did you fall behind in filing your income tax save 20% when you file 3 or more years with us.<br>We can do back to 2012 for filing of tax returns.</p>
    <p>If you expect a refund, the earlier you file the sooner you will receive your refund. Our average turn around time prior to April is a couple of days.</p>
  </section>

  <div class="cta">today so you can start to <strong>breathe easy.</strong><span class="rule"></span></div>

  <section class="bookkeeping">
    <h2>Imagine having your bookkeeping on auto pilot, with<br>everything always up to date and available at your fingertips. Anytime.<br>Anywhere. You’ll always know exactly where you stand with your cash<br>flow—how much you have, owe, are owed, and have made.</h2>
    <p class="feel">How will you feel? Calm, relaxed, and able to make good business decisions. And you’ll<br>have more time to work on your business. In short, you’ll be able to <strong>breathe easy.</strong></p>
    <p class="note">Sound too good to be true? That’s exactly how our clients feel once all their bookkeeping stresses are gone</p>
  </section>

  <div class="contact-label">Contact us:</div>
  <div class="contact">
    <span class="item">
      <svg viewBox="0 0 24 24" aria-hidden="true"><circle cx="12" cy="12" r="12" fill="#fff"/><rect x="6" y="8" width="12" height="8.5" rx="1" fill="none" stroke="#0b93d6" stroke-width="1.5"/><polyline points="6.5,8.5 12,13 17.5,8.5" fill="none" stroke="#0b93d6" stroke-width="1.5"/></svg>
      hello@ledgermint.ca
    </span>
    <span class="divider"></span>
    <span class="item">
      <svg viewBox="0 0 24 24" aria-hidden="true"><circle cx="12" cy="12" r="12" fill="#fff"/><path d="M8.6 6.2l1.8-.4 1.3 3-1.2 1c.6 1.3 1.6 2.4 2.9 3l1-1.2 3 1.3-.4 1.8c-.2.6-.8 1-1.4 1C11 15.4 7.8 12.2 7.6 7.6c0-.6.4-1.2 1-1.4z" fill="#0b93d6"/></svg>
      555-201-4470
    </span>
  </div>
</main>
</body>
</html>
```